Window Treatment business needs website redesigned.

We need a revamp and refresh of our current site www.velmarblinds.ca
Looking to attract very high end customer. It should be a very simple design with very little text. This site will be visited by prospective homeowners, designers, builders and architects. They should feel that they are dealing with a high-end product selection, where experience, customer service and unique product offering is the focus. The content will be to highlight our services and highlight the manufacturers we sell, using a few rich photos to highlight the products. We should NOT look like we are a very large company. It should NOT have discounts/savings buttons and many menus to choose from. We offer over 15 years experience to narrow the many market options, to provide the right technical solution.
We specialize in products that are not readily available on the market and specifically motorized systems for indoors and outdoors.
Our main suppliers are Kervanto.com, Brindex.com
We carry our own locally manufactured product line of roller shades.
Main product pictures should be of roller shades, outdoor bug screens, awnings and outdoor pergolas.

Reason: I understand that Christmas is coming up real short and many people are extremely busy. If you have a CREATIVE gifting you still want to submit, I look forward to your idea!

Reason: Due to holiday season, we have not had sufficient time to review to make a final decision. Thank you for your patience!

Target Market(s)

High end home owners, designers, builders, architects

Industry/Entity Type

Contractor

Coding

Coded - Design and coding required

Number of Pages Required

3 page

Font styles to use
Sans Serif

Requirements
Must have
• Landing page with full size image like homepage of zolvane.it
• Products page that highlights products with simple product shot image, description and link to manufacturer.
• On main page a scrolling of customer reviews.
• I want a very simple, eye-catching, emotional image for homepage. It does not need to include any product image.
• An image that shows technology combining/meshing with hand craftsmanship.
• Focus is on design.
• http://www.zolvane.it/en/gallery is a great layout and design.
Nice to have
• Logo shape for icons and watermark should be used.
• Look like and have simple motion effects like quorix.com or mentaly7.com
Should not have
• Generic/standard looking feel like fellowpine.com or dimworksblinds.ca
• No use of green as background only subtle text.
• Lots of text and pages.

```html
<!DOCTYPE html>
<html lang="en">
<head>
<meta charset="utf-8">
<title>Velmar — Window Treatment Solutions</title>
<link href="https://fonts.googleapis.com/css2?family=Lato:wght@400;700&display=swap" rel="stylesheet">
<style>
  :root {
    --green: #8cc059;
    --green-dark: #6fa23f;
    --ink: #2b2b2b;
    --grey-text: #666;
    --strip: #ececec;
    --frame: #d8d8d8;
    --footer: #4a4a4a;
    --white: #ffffff;
    --arrow: #b5b5b5;
    --hex-fill: rgba(34, 38, 32, 0.72);
  }
  * { box-sizing: border-box; margin: 0; padding: 0; }
  html, body { width: 1200px; height: 850px; overflow: hidden; }
  body { font-family: "Lato", sans-serif; color: var(--ink); background: var(--white); position: relative; }

  .hero-photo {
    position: absolute; left: 0; top: 0; width: 1200px; height: 600px;
    background:
      linear-gradient(170deg, rgba(214,196,150,0.95) 0%, rgba(214,196,150,0.85) 18%, rgba(214,196,150,0) 30%),
      linear-gradient(90deg, #a88b55 0%, #b59a62 30%, #7f8f6b 45%, #cfe0ec 60%, #b6d3ea 80%, #8fb1cf 100%),
      linear-gradient(180deg, #9ec0dd 0%, #6c8e5a 55%, #4d5b3f 100%);
    background-blend-mode: normal, multiply, normal;
  }

  .site-header {
    position: absolute; left: 0; top: 0; width: 1200px; height: 94px;
    background: rgba(255,255,255,0.88);
  }
  .enquiry { position: absolute; left: 40px; top: 26px; display: flex; align-items: center; gap: 14px; }
  .enquiry-label { font-size: 14px; color: var(--ink); line-height: 1.2; }
  .enquiry-number { font-size: 18px; color: var(--ink); line-height: 1.4; }

  .brand { position: absolute; left: 460px; top: 10px; display: flex; align-items: center; gap: 10px; }
  .brand-mark { width: 70px; height: 70px; border-radius: 50%; border: 4px solid var(--ink); }
  .brand-text { display: flex; flex-direction: column; }
  .brand-name { font-size: 40px; font-weight: 400; color: var(--green-dark); line-height: 1; letter-spacing: 1px; }
  .brand-tagline { font-size: 15px; color: var(--grey-text); margin-top: 4px; }

  .main-nav { position: absolute; right: 37px; top: 31px; display: flex; gap: 12px; }
  .main-nav a { font-size: 19px; color: var(--ink); text-decoration: none; padding: 3px 7px; line-height: 1.3; }
  .main-nav a.is-active { background: var(--green); color: var(--white); font-weight: 700; }

  .hero-caption {
    position: absolute; left: 0; top: 504px; width: 1200px; height: 96px;
    background: rgba(0,0,0,0.55); padding: 10px 0 0 94px; color: var(--white);
  }
  .hero-title { font-size: 39px; font-weight: 700; line-height: 1.2; }
  .hero-subtitle { font-size: 19px; margin-top: 4px; }

  .product-hexes { position: absolute; left: 790px; top: 300px; width: 360px; height: 300px; }
  .product-hexes text { font-family: "Lato", sans-serif; font-size: 17px; fill: var(--white); text-anchor: middle; }

  .gallery-strip {
    position: absolute; left: 0; top: 600px; width: 1200px; height: 210px; background: var(--strip);
  }
  .gallery-card {
    position: absolute; top: 18px; width: 324px; height: 176px; background: var(--frame); padding: 9px;
  }
  .gallery-card .thumb { width: 100%; height: 100%; }
  .thumb-pergola { background: linear-gradient(160deg, #cfd3d6 0%, #6c98c8 35%, #8fb6d8 55%, #6f8a4c 80%, #47602f 100%); }
  .thumb-interior { background: linear-gradient(180deg, #d7dde2 0%, #b7c0c8 25%, #e9c06a 50%, #6b5234 80%, #3e3226 100%); }
  .thumb-facade { background: linear-gradient(135deg, #9fc6ea 0%, #eaf3fb 30%, #5b88bd 55%, #3b5f93 75%, #5c7a45 100%); }
  .gallery-arrow {
    position: absolute; top: 689px; width: 34px; height: 34px; border-radius: 50%; background: var(--arrow);
    display: flex; align-items: center; justify-content: center;
  }

  .site-footer {
    position: absolute; left: 0; top: 810px; width: 1200px; height: 40px; background: var(--footer);
    color: var(--white); font-size: 12px; font-weight: 700;
  }
  .copyright { position: absolute; left: 38px; top: 13px; }
  .footer-nav { position: absolute; left: 532px; top: 13px; display: flex; gap: 10px; }
  .footer-nav a { color: var(--white); text-decoration: none; }
  .social { position: absolute; right: 38px; top: 7px; display: flex; gap: 16px; }
  .social span { width: 26px; height: 26px; border-radius: 50%; background: var(--white); display: block; }
</style>
</head>
<body>
  <div class="hero-photo" role="img" aria-label="Terrace with a motorized outdoor shade and awning overlooking a lake and green hills"></div>

  <header class="site-header">
    <div class="enquiry">
      <svg width="32" height="32" viewBox="0 0 24 24" aria-hidden="true">
        <path fill="#8cc059" d="M6.6 10.8a15.2 15.2 0 0 0 6.6 6.6l2.2-2.2a1 1 0 0 1 1-.25 11.4 11.4 0 0 0 3.6.57 1 1 0 0 1 1 1V20a1 1 0 0 1-1 1A17 17 0 0 1 3 4a1 1 0 0 1 1-1h3.5a1 1 0 0 1 1 1c0 1.25.2 2.45.57 3.57a1 1 0 0 1-.25 1z"/>
      </svg>
      <div>
        <p class="enquiry-label">For Enquiry Call us</p>
        <p class="enquiry-number">+1 555 014 2290</p>
      </div>
    </div>

    <div class="brand">
      <span class="brand-mark"></span>
      <div class="brand-text">
        <span class="brand-name">Velmar</span>
        <span class="brand-tagline">Window Treatment Solutions</span>
      </div>
    </div>

    <nav class="main-nav">
      <a href="#" class="is-active">Home</a>
      <a href="#">Gallery</a>
      <a href="#">Contact</a>
    </nav>
  </header>

  <div class="hero-caption">
    <h1 class="hero-title">Motorized Shades</h1>
    <p class="hero-subtitle">We offer both top-of-the-line and affordable automated blinds.</p>
  </div>

  <svg class="product-hexes" viewBox="0 0 360 300" aria-label="Product categories">
    <g fill="rgba(34,38,32,0.72)" stroke="#ffffff" stroke-width="3">
      <polygon points="81,11 147,48 147,124 81,161 15,124 15,48"/>
      <polygon points="213,11 279,48 279,124 213,161 147,124 147,48"/>
      <polygon points="148,138 214,175 214,251 148,288 82,251 82,175"/>
      <polygon points="280,138 346,175 346,251 280,288 214,251 214,175"/>
    </g>
    <g class="hex-icon" fill="none" stroke="#8cc059" stroke-width="2.5">
      <rect x="68" y="32" width="26" height="6"/>
      <rect x="70" y="38" width="22" height="22"/>
      <line x1="81" y1="60" x2="81" y2="66"/>
    </g>
    <text x="81" y="96">Roller</text>
    <text x="81" y="117">Shades</text>
    <g class="hex-icon" fill="none" stroke="#8cc059" stroke-width="2">
      <rect x="199" y="34" width="28" height="28"/>
      <line x1="206" y1="34" x2="206" y2="62"/><line x1="213" y1="34" x2="213" y2="62"/><line x1="220" y1="34" x2="220" y2="62"/>
      <line x1="199" y1="41" x2="227" y2="41"/><line x1="199" y1="48" x2="227" y2="48"/><line x1="199" y1="55" x2="227" y2="55"/>
    </g>
    <text x="213" y="96">Outdoor</text>
    <text x="213" y="117">Bug Screens</text>
    <g class="hex-icon" fill="none" stroke="#8cc059" stroke-width="2.5">
      <path d="M132 170 L148 158 L164 170 Z"/>
      <line x1="134" y1="170" x2="134" y2="190"/><line x1="148" y1="170" x2="148" y2="190"/><line x1="162" y1="170" x2="162" y2="190"/>
      <line x1="130" y1="191" x2="166" y2="191"/>
    </g>
    <text x="148" y="223">Outdoor</text>
    <text x="148" y="244">Pergolas</text>
    <g class="hex-icon" fill="none" stroke="#8cc059" stroke-width="2.5">
      <path d="M262 166 H298 L302 180 H258 Z"/>
      <line x1="264" y1="180" x2="264" y2="200"/><line x1="296" y1="180" x2="296" y2="200"/>
      <rect x="273" y="188" width="14" height="12"/>
    </g>
    <text x="280" y="230">Awnings</text>
  </svg>

  <section class="gallery-strip">
    <div class="gallery-card" style="left:91px"><div class="thumb thumb-pergola" role="img" aria-label="Aluminium pergola with glass panels above a green valley"></div></div>
    <div class="gallery-card" style="left:438px"><div class="thumb thumb-interior" role="img" aria-label="Lit kitchen interior seen through a large window screen at dusk"></div></div>
    <div class="gallery-card" style="left:786px"><div class="thumb thumb-facade" role="img" aria-label="Glass facade with exterior shades in bright sunlight"></div></div>
  </section>
  <div class="gallery-arrow" style="left:33px">
    <svg width="14" height="14" viewBox="0 0 14 14" aria-label="Previous"><path d="M9 2 L4 7 L9 12" fill="none" stroke="#fff" stroke-width="2.5"/></svg>
  </div>
  <div class="gallery-arrow" style="left:1133px">
    <svg width="14" height="14" viewBox="0 0 14 14" aria-label="Next"><path d="M5 2 L10 7 L5 12" fill="none" stroke="#fff" stroke-width="2.5"/></svg>
  </div>

  <footer class="site-footer">
    <p class="copyright">© 2016, Velmar. All Rights Reserved.</p>
    <nav class="footer-nav">
      <a href="#">Home</a><a href="#">Gallery</a><a href="#">Contact</a>
    </nav>
    <div class="social">
      <span aria-label="Social link"></span>
      <span aria-label="Social link"></span>
      <span aria-label="Social link"></span>
    </div>
  </footer>
</body>
</html>
```